Cyber Security Services Flyer/Datasheet

We are looking for a revamp of our current "Cyber Security Penetration Testing Services Datasheet". We would like a professional/modern datasheet that we can give to our Australian customers that are small to mid-sized business owners.

Please see the attached file "PLEASE READ ME.docx" for more details about the design project. It includes all of the design information. If you have more questions or would like to ask any questions please feel free to ask, we are happy to help.

```html
<!DOCTYPE html>
<html lang="en">
<head>
<meta charset="utf-8">
<title>Penetration Testing Services Data Sheet</title>
<link href="https://fonts.googleapis.com/css2?family=Arimo:ital,wght@0,400;0,700;1,400&family=Roboto:wght@500;700&display=swap" rel="stylesheet">
<style>
:root{
  --stage:#4a4a4d;
  --paper:#ffffff;
  --blue:#2f9fdc;
  --navy:#223f8e;
  --navy-deep:#1c3478;
  --ink:#1b1b1b;
  --rule:#2f9fdc;
}
*{box-sizing:border-box;margin:0;padding:0}
html,body{width:1200px;height:1200px;overflow:hidden;background:var(--stage)}
body{position:relative;font-family:"Arimo",Arial,sans-serif;color:var(--ink)}
.page{position:absolute;top:230px;width:576px;height:740px;background:var(--paper);overflow:hidden}
.page--front{left:16px}
.page--back{left:608px}
.abs{position:absolute}
.heading{font-family:"Roboto",Arial,sans-serif;font-weight:700;color:var(--navy);text-transform:uppercase}

/* front header */
.header-art{position:absolute;left:0;top:0}
.brand{position:absolute;left:30px;top:44px;display:flex;align-items:center;gap:8px;font-family:"Roboto",Arial,sans-serif;font-weight:700;font-size:17px;color:var(--navy);letter-spacing:.5px}
.brand-mark{width:22px;height:22px;background:var(--navy)}
.sheet-title{position:absolute;left:208px;top:21px;width:360px;text-align:center;color:#fff;font-family:"Roboto",Arial,sans-serif;font-weight:700;font-size:20.5px;line-height:24px}

/* front content */
.col-left{position:absolute;left:21px;top:364px;width:255px}
.col-right{position:absolute;left:298px;top:364px;width:262px}
.col-left .heading,.col-right .heading{font-size:20.5px;line-height:24px}
.body-copy{font-size:10.9px;line-height:13.1px;margin-top:12px}
.service-list{list-style:none;margin-top:16px}
.service-list li{font-size:10.8px;height:22px;display:flex;align-items:flex-start;gap:6px}
.service-list svg{flex:none;margin-top:1px}
.why{margin-top:18px}
.why p{font-size:9.9px;line-height:12px;margin-top:6px}
.why p + p{margin-top:4px}
.testimonial{margin-top:14px}
.quote-rule{display:flex;align-items:center;justify-content:center;gap:8px;width:210px;margin-left:8px}
.quote-rule span{flex:1;height:1.5px;background:var(--rule)}
.quote-mark{font-family:"Roboto",Arial,sans-serif;font-weight:700;color:var(--navy);font-size:20px;line-height:14px;height:12px}
.testimonial blockquote{font-style:italic;font-size:9.7px;line-height:12px;margin-top:8px}
.testimonial cite{display:block;text-align:right;font-style:normal;font-weight:700;color:var(--navy);font-size:10px;margin-top:8px;padding-right:13px}

/* footer */
.footer{position:absolute;left:0;bottom:0;width:576px;height:51px}
.footer svg{position:absolute;left:0;top:0}
.footer-contact{position:absolute;left:44px;top:16px;color:#fff;font-size:12.4px;letter-spacing:.2px}
.footer-social{position:absolute;right:22px;top:14px;display:flex;align-items:center;gap:5px;color:#fff;font-family:"Roboto",Arial,sans-serif;font-weight:700;font-size:17px}
.footer-social i{display:block;width:14px;height:14px;background:#fff}

/* back */
.top-band{position:absolute;left:0;top:0;width:576px;height:15px;background:var(--blue)}
.process-art{position:absolute;left:0;top:0}
.process-intro{position:absolute;left:26px;top:108px;width:200px}
.process-intro .heading{font-size:13.4px;line-height:16px}
.process-intro p{font-size:10.3px;line-height:13.1px;margin-top:12px}
.process-intro p + p{margin-top:4px}
.step{position:absolute;left:320px;width:222px;color:#fff;font-size:7.6px;line-height:10px}
.step b{font-weight:700}
.section-rule{position:absolute;left:0;width:576px;display:flex;align-items:center;gap:8px}
.section-rule span{flex:1;height:2px;background:var(--rule)}
.section-rule h2{font-family:"Roboto",Arial,sans-serif;font-weight:700;color:var(--navy);font-size:16.5px}
.options{position:absolute;left:0;top:418px;width:576px}
.option{position:absolute;width:170px;text-align:center}
.option svg{display:block;margin:0 auto}
.option h3{font-family:"Roboto",Arial,sans-serif;font-weight:700;color:var(--navy);font-size:13px;line-height:15px;margin-top:8px}
.option p{font-size:10.4px;line-height:13px;margin-top:2px}
.services{position:absolute;left:10px;top:596px;width:556px;display:flex;justify-content:space-between}
.service{width:90px;text-align:center;font-size:10.4px;line-height:12.5px}
.service svg{display:block;margin:0 auto 5px}
</style>
</head>
<body>

<!-- FRONT PAGE -->
<section class="page page--front">
  <svg class="header-art" width="576" height="360" viewBox="0 0 576 360">
    <defs>
      <linearGradient id="photoTone" x1="0" y1="0" x2="1" y2="1">
        <stop offset="0" stop-color="#6b5a4c"/>
        <stop offset=".45" stop-color="#c9c2b8"/>
        <stop offset=".75" stop-color="#b8d8ea"/>
        <stop offset="1" stop-color="#e8d7a6"/>
      </linearGradient>
    </defs>
    <rect x="0" y="78" width="576" height="272" fill="url(#photoTone)" role="img" aria-label="Photo: hands typing on a laptop showing a cyber security login screen on a desk"/>
    <polygon points="0,0 205,0 180,119 0,119" fill="#fff"/>
    <polygon points="205,0 216,0 191,119 180,119" fill="var(--navy)"/>
    <polygon points="0,110 182,110 180,119 0,119" fill="var(--navy)"/>
    <polygon points="216,0 576,0 576,78 200,78" fill="var(--blue)"/>
    <path d="M0,300 L262,324 L576,294 L576,360 L0,360 Z" fill="var(--navy)"/>
    <path d="M0,334 L276,349 L576,330 L576,360 L0,360 Z" fill="#fff"/>
  </svg>
  <div class="brand"><span class="brand-mark"></span>BASTION CYBER</div>
  <h1 class="sheet-title">PENETRATION TESTING SERVICES<br>DATA SHEET</h1>

  <div class="col-left">
    <h2 class="heading">What is Penetration Testing</h2>
    <p class="body-copy">Penetration Testing is the process of simulating real-world attacks by using the same techniques as malicious hackers. Penetration Testing is one of the most comprehensive ways for organisations to develop an understanding of the level of cyber security risk that they carry. Understanding these risks allows organisations to meet industry compliance and regulatory requirements. Additionally, penetration testing allows organisations to develop strategies for the management and remediation of vulnerabilities to reduce overall risk to their business and sensitive data.</p>
    <div class="testimonial">
      <div class="quote-rule"><span></span><div class="quote-mark">&ldquo;</div><span></span></div>
      <blockquote>&ldquo;Bastion Cyber provided well written and easy-to-read reports. The remarkable services provided by the Bastion Cyber team greatly increased the security posture of our environment.&rdquo;</blockquote>
      <cite>-Dan Walsh, General Manager</cite>
    </div>
  </div>

  <div class="col-right">
    <h2 class="heading">Penetration Testing Services</h2>
    <ul class="service-list">
      <li><svg width="9" height="11" viewBox="0 0 9 11"><path d="M1,1 L7,5.5 L1,10" fill="none" stroke="var(--navy)" stroke-width="2.4"/></svg>External Network Testing</li>
      <li><svg width="9" height="11" viewBox="0 0 9 11"><path d="M1,1 L7,5.5 L1,10" fill="none" stroke="var(--navy)" stroke-width="2.4"/></svg>Internal Network Testing</li>
      <li><svg width="9" height="11" viewBox="0 0 9 11"><path d="M1,1 L7,5.5 L1,10" fill="none" stroke="var(--navy)" stroke-width="2.4"/></svg>Web Application Testing</li>
      <li><svg width="9" height="11" viewBox="0 0 9 11"><path d="M1,1 L7,5.5 L1,10" fill="none" stroke="var(--navy)" stroke-width="2.4"/></svg>Wireless Network Testing</li>
      <li><svg width="9" height="11" viewBox="0 0 9 11"><path d="M1,1 L7,5.5 L1,10" fill="none" stroke="var(--navy)" stroke-width="2.4"/></svg>Phishing Testing and Awareness Training</li>
      <li><svg width="9" height="11" viewBox="0 0 9 11"><path d="M1,1 L7,5.5 L1,10" fill="none" stroke="var(--navy)" stroke-width="2.4"/></svg>Monthly Vulnerability Assessments</li>
    </ul>
    <div class="why">
      <h2 class="heading" style="font-size:17px;line-height:20px">Why Choose Bastion Cyber</h2>
      <p>Our team has extensive Offensive Cyber Security experience, holding industry recognised certifications and regularly contributing to the penetration testing community.</p>
      <p>We understand Australian business requirements and are committed to delivering the highest level of customer satisfaction.</p>
    </div>
  </div>

  <footer class="footer">
    <svg width="576" height="51" viewBox="0 0 576 51">
      <rect width="576" height="51" fill="var(--blue)"/>
      <polygon points="410,0 576,0 576,51 432,51" fill="var(--navy)"/>
      <polygon points="402,0 410,0 432,51 424,51" fill="#fff"/>
    </svg>
    <div class="footer-contact">bastioncyber.com.au &nbsp;|&nbsp; hello@bastioncyber.com.au</div>
    <div class="footer-social">Networkly<i></i></div>
  </footer>
</section>

<!-- BACK PAGE -->
<section class="page page--back">
  <div class="top-band"></div>
  <svg class="process-art" width="576" height="380" viewBox="0 0 576 380">
    <defs>
      <linearGradient id="stepFill" x1="0" y1="0" x2="1" y2="1">
        <stop offset="0" stop-color="#2f8bd0"/>
        <stop offset=".6" stop-color="#234a9a"/>
        <stop offset="1" stop-color="#1c3478"/>
      </linearGradient>
    </defs>
    <circle cx="75" cy="197" r="172" fill="none" stroke="var(--navy)" stroke-width="1.5"/>
    <g stroke="var(--navy)" stroke-width="1.5">
      <line x1="193" y1="72" x2="275" y2="55"/>
      <line x1="230" y1="126" x2="264" y2="119"/>
      <line x1="246" y1="201" x2="264" y2="197"/>
      <line x1="230" y1="266" x2="261" y2="262"/>
      <line x1="191" y1="320" x2="262" y2="315"/>
    </g>
    <g fill="var(--blue)">
      <circle cx="193" cy="72" r="7"/><circle cx="230" cy="126" r="7"/><circle cx="246" cy="201" r="7"/><circle cx="230" cy="266" r="7"/><circle cx="191" cy="320" r="7"/>
    </g>
    <g fill="url(#stepFill)">
      <polygon points="300,37 543,37 543,72 300,72 312,54"/>
      <polygon points="298,97 543,97 543,142 298,142 312,119"/>
      <polygon points="299,166 543,166 543,212 299,212 313,189"/>
      <polygon points="296,239 543,239 543,284 296,284 310,261"/>
      <polygon points="297,298 543,298 543,344 297,344 311,321"/>
    </g>
    <g fill="#9bd0f0">
      <polygon points="294,31 318,55 294,79 298,55"/>
      <polygon points="292,95 316,119 292,143 296,119"/>
      <polygon points="293,165 317,189 293,213 297,189"/>
      <polygon points="290,238 314,262 290,286 294,262"/>
      <polygon points="291,297 315,321 291,345 295,321"/>
    </g>
    <g fill="var(--navy)">
      <polygon points="294,33 316,55 294,77 272,55"/>
      <polygon points="292,97 314,119 292,141 270,119"/>
      <polygon points="293,167 315,189 293,211 271,189"/>
      <polygon points="290,240 312,262 290,284 268,262"/>
      <polygon points="291,299 313,321 291,343 269,321"/>
    </g>
    <g fill="#fff" font-family="Roboto,Arial,sans-serif" font-weight="700" font-size="12" text-anchor="middle">
      <text x="294" y="59">1.</text><text x="292" y="123">2.</text><text x="293" y="193">3.</text><text x="290" y="266">4.</text><text x="291" y="325">5.</text>
    </g>
  </svg>

  <div class="step" style="top:39px"><b>SCOPING</b> - An initial meeting will be scheduled whereby one of our experienced consultants will meet with you to determine your security requirements</div>
  <div class="step" style="top:99px"><b>PLANNING</b> – A proposal is developed detailing the specifics of penetration testing. Including recommendations to ensure that industry specific compliance requirements are met.</div>
  <div class="step" style="top:179px"><b>DISCOVERY</b> - The penetration testing is conducted to check for vulnerabilities in the environment.</div>
  <div class="step" style="top:247px"><b>REPORTING</b> – Detailed findings outlining risk level, impact and recommendations is delivered in a written report.</div>
  <div class="step" style="top:300px"><b>DEBRIEFING</b> - Following the delivery of the report one of our experienced consultants will meet with your representatives to discuss outcomes of report and remediation steps.</div>

  <div class="process-intro">
    <h2 class="heading">Client Engagement<br>Process</h2>
    <p>At Bastion Cyber we believe that it is important to keep our clients well informed during the penetration testing process.</p>
    <p>The penetration testing process is to use multiple testing methods including both automated and manual testing in an attempt to gain access to the system and/or sensitive data stored on the system.</p>
  </div>

  <div class="section-rule" style="top:384px"><span></span><h2>PENETRRATION TESTING OPTIONS</h2><span style="flex:.3"></span></div>

  <div class="options">
    <div class="option" style="left:8px">
      <svg width="52" height="52" viewBox="0 0 52 52" fill="none" stroke="#111" stroke-width="2">
        <path d="M12,34 a8,8 0 0 1 2,-15 a11,11 0 0 1 21,-1 a8,8 0 0 1 4,16 Z"/>
        <circle cx="25" cy="26" r="5"/><rect x="36" y="4" width="12" height="9"/><rect x="38" y="42" width="10" height="8"/><rect x="4" y="42" width="12" height="8"/>
      </svg>
      <h3>INTERNAL<br>ASSESSMENT</h3>
      <p>replicates insider<br>threat or<br>compromised user</p>
    </div>
    <div class="option" style="left:189px">
      <svg width="56" height="52" viewBox="0 0 56 52" fill="none" stroke="#111" stroke-width="2">
        <rect x="4" y="8" width="48" height="34" rx="2"/><circle cx="28" cy="20" r="7"/><path d="M18,36 a10,8 0 0 1 20,0"/><line x1="20" y1="48" x2="36" y2="48"/><line x1="28" y1="42" x2="28" y2="48"/>
      </svg>
      <h3>EXTERNAL<br>ASSESSMENT</h3>
      <p>replicates eternal<br>threat to<br>find weaknesses</p>
    </div>
    <div class="option" style="left:370px">
      <svg width="74" height="52" viewBox="0 0 74 52" fill="none" stroke="#111" stroke-width="6" stroke-linecap="round">
        <path d="M6,16 a44,44 0 0 1 62,0"/><path d="M17,28 a28,28 0 0 1 40,0"/><circle cx="37" cy="44" r="4" fill="#111" stroke="none"/>
      </svg>
      <h3>WIRELESS<br>ASSESSMENT</h3>
      <p>Finds unsecured and<br>unauhtorized devices</p>
    </div>
  </div>

  <div class="section-rule" style="top:568px"><span></span><h2>OUR SERVICES</h2><span></span></div>

  <div class="services">
    <div class="service"><svg width="36" height="36" viewBox="0 0 36 36" fill="none" stroke="var(--navy)" stroke-width="1.8"><circle cx="16" cy="16" r="12"/><ellipse cx="16" cy="16" rx="5" ry="12"/><line x1="4" y1="16" x2="28" y2="16"/><circle cx="28" cy="28" r="4"/></svg>Web Application Testing</div>
    <div class="service"><svg width="44" height="36" viewBox="0 0 44 36" fill="none" stroke="var(--navy)" stroke-width="1.8"><rect x="3" y="3" width="38" height="24"/><rect x="8" y="8" width="28" height="6"/><line x1="8" y1="20" x2="24" y2="20"/><line x1="16" y1="33" x2="28" y2="33"/></svg>Internal Network Testing</div>
    <div class="service"><svg width="44" height="36" viewBox="0 0 44 36" fill="none" stroke="var(--navy)" stroke-width="1.8"><rect x="8" y="5" width="28" height="22"/><path d="M3,29 h38 l-3,4 h-32 Z"/></svg>External Network Testing</div>
    <div class="service"><svg width="40" height="36" viewBox="0 0 40 36" fill="none" stroke="var(--navy)" stroke-width="3.5" stroke-linecap="round"><path d="M4,12 a23,23 0 0 1 32,0"/><path d="M11,20 a13,13 0 0 1 18,0"/><circle cx="20" cy="29" r="3" fill="var(--navy)" stroke="none"/></svg>Wireless Network Testing</div>
    <div class="service"><svg width="40" height="36" viewBox="0 0 40 36" fill="none" stroke="var(--navy)" stroke-width="1.8"><rect x="10" y="3" width="18" height="30" rx="2"/><rect x="20" y="8" width="16" height="10"/><line x1="16" y1="29" x2="22" y2="29"/></svg>Mobile Application Testing</div>
    <div class="service"><svg width="36" height="36" viewBox="0 0 36 36" fill="none" stroke="var(--navy)" stroke-width="2"><rect x="6" y="2" width="18" height="32" rx="3"/><circle cx="24" cy="16" r="7" fill="#fff"/><path d="M24,12 v4 h3"/></svg>Hardware/Not Testing</div>
  </div>

  <footer class="footer">
    <svg width="576" height="51" viewBox="0 0 576 51">
      <rect width="576" height="51" fill="var(--blue)"/>
      <polygon points="410,0 576,0 576,51 432,51" fill="var(--navy)"/>
      <polygon points="402,0 410,0 432,51 424,51" fill="#fff"/>
    </svg>
    <div class="footer-contact">bastioncyber.com.au &nbsp;|&nbsp; hello@bastioncyber.com.au</div>
    <div class="footer-social">Networkly<i></i></div>
  </footer>
</section>

</body>
</html>
```